Skin care manufacturer looking for packaging design for new skin care brand.

We need a design and logo for a skin care brand to be sold at retail stores and online in the United States and Europe. The design will be for 1.7oz - 2oz serums that will not have a retail box. The name of the brand is Orvia Lune and should be a luxurious brand that is approachable. The brand will consist of 4 face serums - Vitamin C, Collagen, Retinol and Hyaluronic Acid that all contain Dead Sea Minerals. Images shown are for inspiration only. Color of bottles can be varied based on design and bottles can be screen printed or labeled.

```html
<!DOCTYPE html>
<html lang="en">
<head>
<meta charset="utf-8">
<title>Orvia Lune Serum Collection</title>
<link href="https://fonts.googleapis.com/css2?family=Marcellus&family=Poppins:wght@400;500;700;800&display=swap" rel="stylesheet">
<style>
  :root {
    --backdrop-top: #ececec;
    --backdrop-bottom: #e2e2e2;
    --label-ink: #f3efe8;
    --chrome-light: #f4f4f4;
    --chrome-mid: #b9b9bd;
    --chrome-dark: #6d6d73;
    --gold-light: #f7d66b;
    --gold-mid: #c8951f;
    --gold-dark: #7a5608;
    --collagen: #3f8581;
    --collagen-pill: #1d5d60;
    --vitamin-c: #eaa73c;
    --vitamin-c-pill: #f28a1a;
    --hyaluronic: #4b66c6;
    --hyaluronic-pill: #1b45b6;
    --retinol: #9362bb;
    --retinol-pill: #7b3bb1;
  }
  * { margin: 0; padding: 0; box-sizing: border-box; }
  html, body { width: 1200px; height: 900px; overflow: hidden; }
  body {
    background: linear-gradient(180deg, var(--backdrop-top), var(--backdrop-bottom));
    font-family: 'Poppins', sans-serif;
    position: relative;
  }
  .bottle {
    position: absolute;
    top: 40px;
    width: 250px;
    height: 720px;
  }
  .bottle svg { position: absolute; inset: 0; }
  .bottle--collagen { left: 49px; --tint: var(--collagen); --pill: var(--collagen-pill); }
  .bottle--vitamin-c { left: 336px; --tint: var(--vitamin-c); --pill: var(--vitamin-c-pill); }
  .bottle--hyaluronic { left: 619px; --tint: var(--hyaluronic); --pill: var(--hyaluronic-pill); }
  .bottle--retinol { left: 900px; --tint: var(--retinol); --pill: var(--retinol-pill); }
  .glass { fill: var(--tint); }
  .label {
    position: absolute;
    left: 0; right: 0;
    text-align: center;
    color: var(--label-ink);
  }
  .brand-name {
    top: 372px;
    font-family: 'Marcellus', serif;
    font-size: 35px;
    letter-spacing: 0.5px;
    line-height: 1;
  }
  .product-name {
    top: 458px;
    font-weight: 800;
    font-size: 33px;
    letter-spacing: 3px;
    line-height: 1;
  }
  .product-name--two-line {
    top: 430px;
    font-size: 30px;
    letter-spacing: 0.5px;
    line-height: 0.98;
  }
  .serum-pill {
    top: 502px;
    left: 50%;
    transform: translateX(-50%);
    right: auto;
    background: var(--pill);
    border-radius: 12px;
    padding: 2px 10px;
    font-size: 12.5px;
    letter-spacing: 0.6px;
    white-space: nowrap;
  }
  .blurb {
    top: 552px;
    font-size: 12px;
    line-height: 1.35;
    letter-spacing: 0.6px;
    padding: 0 30px;
  }
  .volume {
    top: 628px;
    font-size: 10px;
    font-weight: 700;
    letter-spacing: 0.8px;
  }
</style>
</head>
<body>
  <svg width="0" height="0" style="position:absolute">
    <defs>
      <linearGradient id="chrome" x1="0" x2="1" y1="0" y2="0">
        <stop offset="0" stop-color="var(--chrome-dark)"/>
        <stop offset="0.3" stop-color="var(--chrome-light)"/>
        <stop offset="0.55" stop-color="var(--chrome-mid)"/>
        <stop offset="0.8" stop-color="var(--chrome-light)"/>
        <stop offset="1" stop-color="var(--chrome-dark)"/>
      </linearGradient>
      <linearGradient id="gold" x1="0" x2="1" y1="0" y2="0">
        <stop offset="0" stop-color="var(--gold-dark)"/>
        <stop offset="0.2" stop-color="var(--gold-light)"/>
        <stop offset="0.5" stop-color="var(--gold-mid)"/>
        <stop offset="0.8" stop-color="var(--gold-light)"/>
        <stop offset="1" stop-color="var(--gold-dark)"/>
      </linearGradient>
      <linearGradient id="sheen" x1="0" x2="1" y1="0" y2="0">
        <stop offset="0" stop-color="#000" stop-opacity="0.18"/>
        <stop offset="0.3" stop-color="#fff" stop-opacity="0.12"/>
        <stop offset="0.6" stop-color="#fff" stop-opacity="0"/>
        <stop offset="1" stop-color="#000" stop-opacity="0.15"/>
      </linearGradient>
    </defs>
  </svg>

  <div class="bottle bottle--collagen">
    <svg viewBox="0 0 250 720" width="250" height="720" aria-hidden="true">
      <rect x="90" y="0" width="70" height="125" rx="35" fill="url(#chrome)"/>
      <rect x="60" y="212" width="130" height="20" class="glass"/>
      <path class="glass" d="M65,228 L185,228 C185,262 250,270 250,340 L250,690 Q250,715 225,715 L25,715 Q0,715 0,690 L0,340 C0,270 65,262 65,228 Z"/>
      <path fill="url(#sheen)" d="M65,228 L185,228 C185,262 250,270 250,340 L250,690 Q250,715 225,715 L25,715 Q0,715 0,690 L0,340 C0,270 65,262 65,228 Z"/>
      <rect x="52" y="115" width="146" height="100" rx="4" fill="url(#gold)"/>
    </svg>
    <div class="label brand-name">ORVIA LUNE</div>
    <div class="label product-name">COLLAGEN</div>
    <div class="label serum-pill">BRIGHTENING SERUM</div>
    <p class="label blurb">Lorem Ipsum is simply dummy text of the printing and typesetting industry.</p>
    <div class="label volume">50ML/1.7 FLO OZ</div>
  </div>

  <div class="bottle bottle--vitamin-c">
    <svg viewBox="0 0 250 720" width="250" height="720" aria-hidden="true">
      <rect x="90" y="0" width="70" height="125" rx="35" fill="url(#chrome)"/>
      <rect x="60" y="212" width="130" height="20" class="glass"/>
      <path class="glass" d="M65,228 L185,228 C185,262 250,270 250,340 L250,690 Q250,715 225,715 L25,715 Q0,715 0,690 L0,340 C0,270 65,262 65,228 Z"/>
      <path fill="url(#sheen)" d="M65,228 L185,228 C185,262 250,270 250,340 L250,690 Q250,715 225,715 L25,715 Q0,715 0,690 L0,340 C0,270 65,262 65,228 Z"/>
      <rect x="52" y="115" width="146" height="100" rx="4" fill="url(#gold)"/>
    </svg>
    <div class="label brand-name">ORVIA LUNE</div>
    <div class="label product-name">VITAMIN C</div>
    <div class="label serum-pill">BRIGHTENING SERUM</div>
    <p class="label blurb">Lorem Ipsum is simply dummy text of the printing and typesetting industry.</p>
    <div class="label volume">50ML/1.7 FLO OZ</div>
  </div>

  <div class="bottle bottle--hyaluronic">
    <svg viewBox="0 0 250 720" width="250" height="720" aria-hidden="true">
      <rect x="90" y="0" width="70" height="125" rx="35" fill="url(#chrome)"/>
      <rect x="60" y="212" width="130" height="20" class="glass"/>
      <path class="glass" d="M65,228 L185,228 C185,262 250,270 250,340 L250,690 Q250,715 225,715 L25,715 Q0,715 0,690 L0,340 C0,270 65,262 65,228 Z"/>
      <path fill="url(#sheen)" d="M65,228 L185,228 C185,262 250,270 250,340 L250,690 Q250,715 225,715 L25,715 Q0,715 0,690 L0,340 C0,270 65,262 65,228 Z"/>
      <rect x="52" y="115" width="146" height="100" rx="4" fill="url(#gold)"/>
    </svg>
    <div class="label brand-name">ORVIA LUNE</div>
    <div class="label product-name product-name--two-line">HYALURONIC<br>ACID</div>
    <div class="label serum-pill">BRIGHTENING SERUM</div>
    <p class="label blurb">Lorem Ipsum is simply dummy text of the printing and typesetting industry.</p>
    <div class="label volume">50ML/1.7 FLO OZ</div>
  </div>

  <div class="bottle bottle--retinol">
    <svg viewBox="0 0 250 720" width="250" height="720" aria-hidden="true">
      <rect x="90" y="0" width="70" height="125" rx="35" fill="url(#chrome)"/>
      <rect x="60" y="212" width="130" height="20" class="glass"/>
      <path class="glass" d="M65,228 L185,228 C185,262 250,270 250,340 L250,690 Q250,715 225,715 L25,715 Q0,715 0,690 L0,340 C0,270 65,262 65,228 Z"/>
      <path fill="url(#sheen)" d="M65,228 L185,228 C185,262 250,270 250,340 L250,690 Q250,715 225,715 L25,715 Q0,715 0,690 L0,340 C0,270 65,262 65,228 Z"/>
      <rect x="52" y="115" width="146" height="100" rx="4" fill="url(#gold)"/>
    </svg>
    <div class="label brand-name">ORVIA LUNE</div>
    <div class="label product-name">RETINOL</div>
    <div class="label serum-pill">BRIGHTENING SERUM</div>
    <p class="label blurb">Lorem Ipsum is simply dummy text of the printing and typesetting industry.</p>
    <div class="label volume">50ML/1.7 FLO OZ</div>
  </div>
</body>
</html>
```